Professional BIO Template with photo and logo

Hello,
I need a professional Bio template developed via Microsoft WORD ASAP!!!!! I would like to just be able to add the text I need to add. So resize-able text boxes. Potentially able to adjust the font. These are the things I need added it to include.
Head shot (attached)
Text Box for Name
Text Box for phone number
Text box for email
KTW Logo (attached)
Maybe a blue banner at the top or some background boxes that are blue or grey. Here are the pantone colors that our company uses.

CORE COLOR
100c 91m 17y 6k 38r 58g 128b Hex #263A80 Pantone 7687 C

CORE CONTRAST COLOR
36c 29m 28y 0k 168r 168g 170b Hex #669999 Pantone Cool Gray 6C

I also attached some examples of what we have been looking at. Instead of green add the blue...instead of black maybe just be white.

Thank you

```html
<!DOCTYPE html>
<html lang="en">
<head>
<meta charset="UTF-8">
<title>Evan Marlowe – Bio</title>
<link href="https://fonts.googleapis.com/css2?family=Poppins:ital,wght@0,400;0,500;0,600;0,700;1,500&display=swap" rel="stylesheet">
<style>
  :root {
    --core-blue: #263a80;
    --contrast-teal: #669999;
    --ink: #333333;
    --body-ink: #3a3a3a;
    --quote-bg: #e4e7f0;
    --white: #ffffff;
    --photo-top: #8a8c90;
    --photo-bottom: #3b3f46;
  }
  * { box-sizing: border-box; margin: 0; padding: 0; }
  html, body { width: 927px; height: 1200px; overflow: hidden; background: var(--white); }
  body { font-family: "Poppins", sans-serif; color: var(--body-ink); }
  .bio-sheet { position: relative; width: 927px; height: 1200px; overflow: hidden; background: var(--white); }

  .header-band { position: absolute; left: 0; top: 0; width: 927px; height: 280px; }

  .headshot {
    position: absolute; left: 22px; top: 46px; width: 400px; height: 469px;
    border: 5px solid var(--white); border-radius: 30px;
    background: radial-gradient(ellipse at 50% 35%, var(--photo-top), var(--photo-bottom) 75%);
  }

  .brand-box {
    position: absolute; left: 650px; top: 41px; width: 248px; height: 185px;
    border: 2px solid var(--white);
    display: flex; align-items: center; justify-content: center;
  }
  .brand-name { color: var(--white); font-weight: 600; font-size: 56px; letter-spacing: 4px; }

  .contact { position: absolute; left: 465px; top: 292px; }
  .contact-name { color: var(--ink); font-weight: 600; font-size: 45px; line-height: 1.2; margin-bottom: 8px; }
  .contact-line {
    display: flex; align-items: center; gap: 14px;
    color: var(--core-blue); font-weight: 600; font-size: 30px; line-height: 1.2; margin-bottom: 16px;
  }
  .contact-line svg { width: 26px; height: 26px; fill: var(--core-blue); flex: none; }

  .about { position: absolute; left: 22px; top: 552px; width: 884px; }
  .about-title { color: var(--contrast-teal); font-weight: 600; font-size: 37px; line-height: 1.3; margin-bottom: 6px; }
  .about p { font-size: 17px; line-height: 30.5px; margin-bottom: 8px; }

  .pull-quote {
    background: var(--quote-bg); border-radius: 13px;
    padding: 18px 24px 18px 25px; margin: 20px -1px 22px -1px;
    color: var(--core-blue); font-style: italic; font-weight: 500; font-size: 21.5px; line-height: 35px;
  }

  .footer {
    position: absolute; left: 0; top: 1149px; width: 927px; height: 51px;
    background: var(--core-blue); color: var(--white);
    display: flex; align-items: center; justify-content: center; font-size: 15px;
  }
</style>
</head>
<body>
<main class="bio-sheet">
  <svg class="header-band" viewBox="0 0 927 280" aria-hidden="true">
    <polygon points="0,0 927,0 927,273 0,196" fill="var(--core-blue)"/>
    <polygon points="0,196 423,234 0,273" fill="var(--contrast-teal)"/>
  </svg>

  <div class="headshot" role="img" aria-label="Head shot portrait of Evan Marlowe"></div>

  <div class="brand-box">
    <span class="brand-name">KTW</span>
  </div>

  <section class="contact">
    <h1 class="contact-name">Evan Marlowe</h1>
    <div class="contact-line">
      <svg viewBox="0 0 24 24" aria-hidden="true"><path d="M6.6 10.8a15 15 0 0 0 6.6 6.6l2.2-2.2a1 1 0 0 1 1-.25 11.4 11.4 0 0 0 3.6.57 1 1 0 0 1 1 1V20a1 1 0 0 1-1 1A17 17 0 0 1 3 4a1 1 0 0 1 1-1h3.5a1 1 0 0 1 1 1c0 1.25.2 2.45.57 3.57a1 1 0 0 1-.25 1z"/></svg>
      <span>1-800-555-0142</span>
    </div>
    <div class="contact-line">
      <svg viewBox="0 0 24 24" aria-hidden="true"><path d="M2 5h20v2l-10 6L2 7z M2 9l10 6 10-6v10H2z"/></svg>
      <span>info@evanmarlowe.com</span>
    </div>
  </section>

  <section class="about">
    <h2 class="about-title">About Evan Marlowe</h2>
    <p>Sed ut perspiciatis unde omnis iste natus error sit voluptatem accusantium&nbsp; doloremque laudantium, totam rem aperiam, eaque ipsa quae ab illo inventore veritatis et quasi architecto beatae vitae dicta sunt explicabo.</p>
    <p>Neque porro quisquam est, qui dolorem ipsum quia dolor sit amet, consectetur, adipisci velit, sed quia non numquam eius modi tempora incidunt ut labore et dolore magnam aliquam quaerat voluptatem. Ut enim ad minima veniam.</p>
    <blockquote class="pull-quote">“ Neque porro quisquam est, qui dolorem ipsum quia dolor sit amet, consectetur, adipisci velit, sed quia non numquam eius modi tempora ncidunt ut labore et dolore magnam aliquam quaerat voluptatem.<br>Ut enim ad minima veniam..”</blockquote>
    <p>Sed ut perspiciatis unde omnis iste natus error sit voluptatem accusantium&nbsp; doloremque laudantium, totam rem aperiam, eaque ipsa quae ab illo inventore veritatis et quasi architecto beatae vitae dicta sunt explicabo.</p>
  </section>

  <footer class="footer">Copyright © 2022 Company Name.&nbsp; All Right Reserved</footer>
</main>
</body>
</html>
```